Simple landing page for Brindleys cookbook

I need a one page landingpage where customers can order the cookbook.
This is a cookbook of a collection of recipes from our deli that we used to run.
I need a landing page where customers can come and order the book. I also need it coded. I already have the domain through hostmoxa.
I can send the file of the book through wetransfer. It's too big to upload here. Just so you get the feel that I am looking for.
I attached a simple text as an introduction to the page. But I am open to any suggestions. I want it all to be about the experience that we are sharing the recipes with everybody and that it's for sale. The book is $29.99, shipping included.
Customers have to be able to click and buy the book from it.

Coding

Coded - Design and coding required

Number of Pages Required

1 page

Font styles to use
Sans Serif

Requirements
Must have
• Same colors as the cookbook

```html
<!DOCTYPE html>
<html lang="en">
<head>
<meta charset="utf-8">
<title>Brindleys Cookbook</title>
<link href="https://fonts.googleapis.com/css2?family=Exo+2:wght@600;700&family=Poppins:wght@500;600;700&family=IBM+Plex+Sans:wght@300;400&family=Montserrat:wght@500&display=swap" rel="stylesheet">
<style>
  :root {
    --black: #000000;
    --yellow: #f0b000;
    --amber: #e39a00;
    --white: #ffffff;
    --paper: #f3f3f3;
    --ink: #111111;
    --body-text: #3a3a3a;
    --slate: #a9b4bf;
    --plate: #bcc5cf;
    --plate-inner: #aeb9c5;
    --green: #6cc24a;
    --halo: #d9e3cf;
    --sky: #c9e3f2;
    --navy: #101a3a;
  }
  * { margin: 0; padding: 0; box-sizing: border-box; }
  html, body { width: 997px; height: 1200px; overflow: hidden; background: var(--paper); }
  .page { position: relative; width: 997px; height: 1200px; overflow: hidden; font-family: "IBM Plex Sans", sans-serif; }

  .hero { position: absolute; left: 0; top: 0; width: 997px; height: 563px; background: var(--black); overflow: hidden; }
  .hero-band { position: absolute; left: 0; top: 0; width: 997px; height: 563px; }
  .brand { position: absolute; left: 90px; top: 18px; font-family: "Exo 2", sans-serif; font-weight: 700; font-size: 23px; color: var(--white); letter-spacing: 0.5px; }
  .nav { position: absolute; top: 30px; left: 417px; display: flex; gap: 32px; }
  .nav a { font-family: "Poppins", sans-serif; font-weight: 500; font-size: 16.5px; color: var(--white); text-decoration: none; }
  .nav-pill { position: absolute; left: 791px; top: 23px; width: 124px; height: 37px; border-radius: 19px; background: var(--slate); color: var(--white); font-family: "Poppins", sans-serif; font-weight: 500; font-size: 15px; display: flex; align-items: center; justify-content: center; text-decoration: none; }

  .hero-title { position: absolute; left: 83px; top: 186px; font-family: "Exo 2", sans-serif; font-weight: 700; font-size: 45px; line-height: 55px; color: var(--white); }
  .order-btn { position: absolute; left: 82px; top: 325px; width: 164px; height: 40px; border-radius: 20px; background: var(--white); color: var(--navy); font-family: "Montserrat", sans-serif; font-weight: 500; font-size: 14.5px; display: flex; align-items: center; justify-content: center; text-decoration: none; letter-spacing: 0.3px; }

  .halo { position: absolute; left: 523px; top: 167px; width: 400px; height: 400px; border-radius: 50%; background: var(--halo); }
  .halo-inner { position: absolute; left: 566px; top: 205px; width: 360px; height: 360px; border-radius: 50%; background: var(--sky); }
  .burger-photo { position: absolute; left: 565px; top: 172px; width: 432px; height: 391px; border-radius: 190px 0 0 0; background: radial-gradient(ellipse at 60% 35%, #e0902c 0%, #c4702a 35%, #7a4a2a 75%, #4a3020 100%); }

  .badge { position: absolute; width: 88px; height: 88px; border-radius: 50%; background: var(--white); border: 2px solid var(--green); display: flex; flex-direction: column; align-items: center; justify-content: center; text-align: center; color: #2a1a10; font-family: "Poppins", sans-serif; font-weight: 600; }
  .badge-price { left: 539px; top: 184px; }
  .badge-price .label { font-size: 14px; line-height: 18px; }
  .badge-price .amount { font-family: "Exo 2", sans-serif; font-size: 19px; line-height: 26px; }
  .badge-fresh { left: 480px; top: 349px; font-size: 13px; line-height: 18px; }

  .intro { position: absolute; left: 0; top: 563px; width: 997px; height: 591px; background: var(--paper); }
  .plate { position: absolute; left: 33px; top: 733px; width: 358px; height: 358px; border-radius: 50%; background: var(--plate); }
  .plate-inner { position: absolute; left: 70px; top: 770px; width: 284px; height: 284px; border-radius: 50%; background: var(--plate-inner); }
  .book-cover { position: absolute; left: 100px; top: 680px; width: 220px; height: 385px; transform: rotate(15deg); transform-origin: center; background: linear-gradient(180deg, #dcecf6 0%, #f2f5f8 25%, #d79a4a 50%, #c9d6de 80%, #eef2f5 100%); box-shadow: 6px 4px 0 #2a2a2a; }

  .intro-copy { position: absolute; left: 417px; top: 624px; width: 500px; }
  .intro-copy h1 { font-family: "Poppins", sans-serif; font-weight: 700; font-size: 25px; color: var(--ink); letter-spacing: 0.4px; line-height: 34px; }
  .intro-copy h2 { font-family: "Poppins", sans-serif; font-weight: 600; font-size: 20.5px; color: var(--ink); letter-spacing: 0.4px; margin-top: 13px; line-height: 30px; }
  .intro-copy p { font-weight: 300; font-size: 14.3px; line-height: 21.4px; color: var(--body-text); margin-top: 10px; }
  .intro-copy h2 + p { margin-top: 22px; }

  .footer { position: absolute; left: 0; top: 1154px; width: 997px; height: 46px; background: var(--black); display: flex; align-items: center; justify-content: center; font-family: "Montserrat", sans-serif; font-weight: 500; font-size: 14.5px; color: var(--white); }
</style>
</head>
<body>
<div class="page">
  <header class="hero">
    <svg class="hero-band" role="img" aria-label="Yellow brush-stroke splash across the hero" viewBox="0 0 997 563" width="997" height="563">
      <defs>
        <linearGradient id="splash" x1="0" y1="0" x2="0" y2="1">
          <stop offset="0" stop-color="#f2b600"/>
          <stop offset="1" stop-color="#e39a00"/>
        </linearGradient>
      </defs>
      <polygon points="0,165 997,55 997,430 0,530" fill="url(#splash)"/>
    </svg>

    <div class="brand">BRINDLEYS</div>
    <nav class="nav">
      <a href="#">Home</a>
      <a href="#intro">About</a>
      <a href="#order">Pricing</a>
      <a href="#">Contact</a>
    </nav>
    <a class="nav-pill" href="#order">Brindleys</a>

    <h1 class="hero-title">Welcome to<br>Brindleys Cookbook</h1>
    <a class="order-btn" id="order" href="#order">ORDER NOW</a>

    <div class="halo"></div>
    <div class="halo-inner"></div>
    <div class="burger-photo" role="img" aria-label="Photo of a sesame burger with peppers, spinach and cheese on a wooden board"></div>

    <div class="badge badge-price"><span class="label">Pricing</span><span class="amount">$29.99</span></div>
    <div class="badge badge-fresh"><span>fresh</span><span>&amp;</span><span>tasty</span></div>
  </header>

  <section class="intro" id="intro"></section>
  <div class="plate"></div>
  <div class="plate-inner"></div>
  <div class="book-cover" role="img" aria-label="Brindleys sandwiches cookbook cover showing a sandwich"></div>

  <div class="intro-copy">
    <h1>BRINDLEYS COOKBOOK</h1>
    <h2>INTRODUCTION</h2>
    <p>Opening it’s doors in January of 2010, Brindleys European Deli was a sandwich shop in Harrowgate, Nova Ridge, but also a lot more than that.</p>
    <p>We spent five years with this business until it’s eventual closure in April of 2015. It was a special time where we met tons of amazing people, who we loved to see and serve.</p>
    <p>Brindleys started out as a deli but eventually morphed into the sandwich shop we all know it as today.</p>
    <p>We are overwhelmed with the continuous positive messages and comments we get on our Chatterly page that is still up and running.</p>
    <p>Unfortunately, we can’t open another Brindleys, but we can offer you this collection of our recipes for you to try out at home with your family and friends.</p>
    <p>We truly hope you will enjoy making these sandwiches just as much as we did.</p>
    <p>If you do, please post your pictures of you making a meal or the finished product, or even enjoying it!</p>
  </div>

  <footer class="footer">© copyrights 2022 Brindleys Cookbook&nbsp; | &nbsp;All Rights Reserved</footer>
</div>
</body>
</html>
```